Design a menu for a Pizza company

I need help designing a color menu for a pizza company. It will be a 9x16" trifold menu (3-panel). I would like to include some photos of pizza, salads, subs, sandwiches, drinks, etc. (no clipart). Attached is an example of an existing menu. I need to make the menu full color. We would like to modernize this menu with full color photos like the attached sample menu. The final files should have editable files so I can edit prices and menu items as needed. I prefer CorelDraw graphics software.

Target Market(s)

General public.

Industry/Entity Type

Restaurant

Font styles to use
Sans Serif

Colors
ec1f27
fffefc
9bcb3b

Requirements
Must have
• Must have photos and editable fonts. I will need to be able to edit the contents of the menu after you provide me with the final files.
Nice to have
• It would be nice to have this menu created in CorelDraw X7 or X8.
Should not have
• Should not have clip art or low resolution photos.

```html
<!DOCTYPE html>
<html lang="en">
<head>
<meta charset="utf-8">
<title>Forno Pizza – Trifold Menu</title>
<link rel="stylesheet" href="https://fonts.googleapis.com/css2?family=Oswald:wght@500;600&family=Roboto+Condensed:ital,wght@0,400;0,500;1,400&display=swap">
<style>
  :root {
    --red: #ec1f27;
    --white: #fffefc;
    --green: #9bcb3b;
    --yellow: #f7ec13;
    --ink: #1b1b1b;
    --stage: #5b3a10;
    --panel-light: #f4f9d6;
    --panel-mid: #dcefa6;
  }
  * { box-sizing: border-box; margin: 0; padding: 0; }
  html, body { width: 1200px; height: 1200px; overflow: hidden; }
  body { background: var(--stage); font-family: "Roboto Condensed", sans-serif; color: var(--ink); }

  .spread {
    position: absolute; left: 30px; top: 277px;
    width: 1140px; height: 645px; display: flex;
    box-shadow: 0 10px 30px rgba(0,0,0,.45);
  }
  .panel { position: relative; width: 380px; height: 645px; overflow: hidden; }
  .panel--menu {
    background: radial-gradient(ellipse at 50% 40%, var(--white) 0%, var(--panel-light) 45%, var(--panel-mid) 100%);
  }
  .panel--menu + .panel--menu { border-left: 1px solid rgba(0,0,0,.08); }

  .photo { position: absolute; border-radius: 50%; z-index: 1; }

  .section-title {
    position: absolute; left: 62px; width: 250px; text-align: center;
    font-family: "Oswald", sans-serif; font-weight: 600; font-size: 16px;
    color: var(--red); line-height: 1; transform: translateY(-50%); z-index: 2;
  }
  .section-title.small { font-size: 13px; left: 20px; width: 200px; }
  .rule {
    position: absolute; left: 62px; width: 250px; height: 3px;
    background: linear-gradient(90deg, transparent, var(--red) 30%, var(--red) 70%, transparent);
    opacity: .75; z-index: 2;
  }
  .rule.small { left: 20px; width: 200px; }
  .note {
    position: absolute; left: 40px; width: 295px; text-align: center;
    font-style: italic; font-size: 9px; line-height: 1; color: #333;
    transform: translateY(-50%); z-index: 2;
  }
  .item, .price {
    position: absolute; font-size: 11.5px; font-weight: 500; line-height: 1;
    white-space: nowrap; transform: translateY(-50%); z-index: 2;
  }
  .item { left: 27px; }
  .item.upper { text-transform: uppercase; }
  .cols { position: absolute; font-size: 11.5px; font-weight: 500; transform: translateY(-50%); line-height: 1; z-index: 2; white-space: nowrap; }

  .panel--cover { background: var(--red); }
  .brand-name {
    position: absolute; left: 40px; top: 36px; width: 300px; text-align: center;
    font-family: "Oswald", sans-serif; font-weight: 600; font-size: 62px; line-height: 1.1;
    color: var(--yellow);
  }
  .chef-art { position: absolute; left: 29px; top: 149px; width: 323px; height: 340px; border-radius: 40%; }
  .info-band { position: absolute; left: 0; top: 491px; width: 380px; height: 154px; background: var(--green); }
  .open-box {
    position: absolute; left: 2px; top: 33px; width: 107px; height: 104px;
    background: #111; color: var(--white); font-family: "Oswald", sans-serif; font-weight: 500;
    font-size: 19px; line-height: 1.2; padding: 8px 0 0 26px;
  }
  .open-box .open { color: var(--red); font-size: 26px; line-height: 1.05; }
  .edge-bar { position: absolute; right: 0; top: 33px; width: 9px; height: 104px; background: #111; }
  .hours {
    position: absolute; left: 116px; width: 248px; top: 39px; text-align: center;
    font-size: 11.5px; font-weight: 500; line-height: 16px;
  }
  .hours .accent { color: var(--yellow); font-size: 13px; }
  .hours .service { color: var(--yellow); font-family: "Oswald", sans-serif; font-weight: 500; font-size: 21px; line-height: 26px; }
</style>
</head>
<body>
<main class="spread">

  <!-- Panel 1: dinners & kids -->
  <section class="panel panel--menu">
    <div class="rule" style="top:23px"></div>
    <h2 class="section-title" style="top:39px">ITALIAN DINNERS</h2>
    <div class="rule" style="top:52px"></div>
    <p class="note" style="top:65px">Served on Garlic Bread &amp; Salad</p>
    <p class="note" style="top:75px">Choice of Dressing :</p>
    <p class="note" style="top:85px">Ranch, French, Italian, Blue Cheese, Thousand Island</p>

    <span class="item" style="top:108px">Spaghetti w/ Meat Sauce</span><span class="price" style="top:108px;left:234px">8.99</span>
    <span class="item" style="top:134px">Spaghetti w/ Meatballs</span><span class="price" style="top:134px;left:234px">9.99</span>
    <span class="item" style="top:160px">Veal Parmigiana w/ Spaghetti</span><span class="price" style="top:160px;left:234px">9.99</span>
    <span class="item" style="top:185px">Chicken Parmigiana w/ Spaghetti</span><span class="price" style="top:185px;left:234px">9.99</span>
    <span class="item" style="top:211px">Eggplant Parmigiana w/ Spaghetti</span><span class="price" style="top:211px;left:234px">9.99</span>
    <span class="item" style="top:236px">Baked Lasagna</span><span class="price" style="top:236px;left:234px">9.99</span>
    <span class="item" style="top:262px">Ravioli w/ Meat Sauce</span><span class="price" style="top:262px;left:234px">9.99</span>

    <div class="photo" role="img" aria-label="Plate of spaghetti with meat sauce" style="left:257px;top:96px;width:124px;height:128px;background:radial-gradient(circle,#b5401f 0%,#d9a253 45%,#f3e4b8 70%,transparent 72%)"></div>

    <div class="rule" style="top:275px"></div>
    <h2 class="section-title" style="top:288px">SEAFOOD DINNERS</h2>
    <div class="rule" style="top:301px"></div>
    <p class="note" style="top:314px">Served with Garlic Bread, French Fries &amp; Salad</p>
    <p class="note" style="top:326px">Choice of Dressing :</p>
    <p class="note" style="top:338px">Ranch, French, Italian, Blue Cheese, Thousand Island</p>

    <span class="item" style="top:361px">Shrimp Basket</span><span class="price" style="top:361px;left:234px">8.99</span>
    <span class="item" style="top:386px">Crab Cake</span><span class="price" style="top:386px;left:229px">10.99</span>
    <span class="item" style="top:410px">Fish Filet</span><span class="price" style="top:410px;left:229px">10.99</span>

    <div class="photo" role="img" aria-label="Stacked golden crab cakes on greens" style="left:277px;top:312px;width:84px;height:106px;background:radial-gradient(circle,#d79a3a 0%,#e8c56e 45%,#a9c86a 68%,transparent 72%)"></div>

    <div class="rule" style="top:424px"></div>
    <h2 class="section-title" style="top:436px">CHILDREN'S MENU</h2>
    <div class="rule" style="top:449px"></div>

    <span class="item" style="top:463px">Chicken Tenders w/ French Fries ...............</span><span class="price" style="top:463px;left:234px">5.99</span>
    <span class="item" style="top:487px">Spaghetti w/ Meat Sauce ..........................</span><span class="price" style="top:487px;left:234px">5.99</span>
    <span class="item" style="top:513px">Ravioli w/ Meat Sauce ..............................</span><span class="price" style="top:513px;left:234px">5.99</span>
    <span class="item" style="top:537px">Shrimp w/ French Fries ............................</span><span class="price" style="top:537px;left:234px">5.99</span>
    <span class="item" style="top:563px">*Cheeseburger w/ French Fries &amp; small Beverage ..........</span><span class="price" style="top:563px;left:302px">5.99</span>

    <div class="photo" role="img" aria-label="Carton of french fries" style="left:290px;top:447px;width:64px;height:104px;border-radius:12px;background:linear-gradient(180deg,#f2c53d 0%,#f2c53d 45%,#e3262c 46%,#fffefc 100%)"></div>
    <div class="photo" role="img" aria-label="Chicken tenders and fries with dipping sauce" style="left:0;top:560px;width:125px;height:85px;background:radial-gradient(ellipse,#d99a3e 0%,#eac06a 50%,#f5ead0 70%,transparent 74%)"></div>

    <p class="note" style="top:588px;left:120px;width:220px;text-align:right">* These Items Are Cooked To Order.</p>
    <p class="note" style="top:599px;left:100px;width:240px;text-align:right">"Consuming Raw Or Undercooked Meats May Increase</p>
    <p class="note" style="top:609px;left:120px;width:175px;text-align:right">Your Risk Of Foodborne Illness."</p>
  </section>

  <!-- Panel 2: drinks -->
  <section class="panel panel--menu">
    <div class="rule" style="top:24px"></div>
    <h2 class="section-title" style="top:39px">SODA</h2>
    <div class="rule" style="top:52px"></div>

    <span class="item upper" style="top:66px">Pitcher ..........................3.99</span>
    <span class="item upper" style="top:89px">Cola</span>
    <span class="cols" style="top:89px;left:147px">12 oz....16 oz....24 oz....32 oz.</span>

    <span class="item upper" style="top:113px">Cola ............................</span>
    <span class="item upper" style="top:137px">Lemon-Lime ................</span>
    <span class="item upper" style="top:161px">Root Beer ..................</span>
    <span class="item upper" style="top:185px">Diet Cola ...................</span>
    <span class="cols" style="top:113px;left:155px">99 &nbsp;.... &nbsp;1.30 ....1.69 .... 1.99</span>
    <span class="cols" style="top:137px;left:155px">99 &nbsp;.... &nbsp;1.30 ....1.69 .... 1.99</span>
    <span class="cols" style="top:161px;left:155px">99 &nbsp;.... &nbsp;1.30 ....1.69 .... 1.99</span>
    <span class="cols" style="top:185px;left:155px">99 &nbsp;.... &nbsp;1.30 ....1.69 .... 1.99</span>

    <div class="photo" role="img" aria-label="Cola bottle with splash" style="left:314px;top:56px;width:62px;height:136px;border-radius:30px;background:radial-gradient(ellipse,#6a1d10 0%,#a6522a 45%,#e3b06d 65%,transparent 72%)"></div>

    <div class="rule" style="top:201px"></div>
    <h2 class="section-title" style="top:213px">BEVERAGES</h2>
    <div class="rule" style="top:226px"></div>
    <span class="item upper" style="top:242px">Iced Tea........................................</span>
    <span class="cols" style="top:242px;left:205px">16 oz. ...... 24 oz. ...... 32 oz.</span>
    <span class="cols" style="top:265px;left:208px">1.30 &nbsp;...... &nbsp;1.69 &nbsp;...... &nbsp;1.99</span>

    <div class="rule" style="top:284px"></div>
    <h2 class="section-title" style="top:297px">BEER</h2>
    <div class="rule" style="top:309px"></div>

    <span class="item upper" style="top:323px;font-weight:600">Draft</span>
    <span class="item upper" style="top:347px">32 oz. Pitcher........................ 6.99</span>
    <span class="item upper" style="top:371px">60 oz. Pitcher.......................10.99</span>
    <span class="item upper" style="top:394px">Harbor Lager........................ 2.60</span>

    <div class="rule small" style="top:408px"></div>
    <h2 class="section-title small" style="top:418px">BOTTLES</h2>
    <div class="rule small" style="top:428px"></div>
    <span class="item upper" style="top:442px">Harbor Lager........................ 3.25</span>
    <span class="item upper" style="top:466px">Mill Creek............................. 3.25</span>
    <span class="item upper" style="top:490px">Mill Creek Lite...................... 3.25</span>
    <span class="item upper" style="top:513px">Peak Gold............................ 3.25</span>
    <span class="item upper" style="top:537px">Peak Light........................... 3.25</span>

    <div class="rule small" style="top:550px"></div>
    <h2 class="section-title small" style="top:561px">IMPORTED BOTTLES</h2>
    <div class="rule small" style="top:572px"></div>
    <span class="item upper" style="top:585px">Dutch Green......................... 3.75</span>
    <span class="item upper" style="top:609px">Playa Clara.......................... 3.75</span>

    <div class="photo" role="img" aria-label="Glass of amber beer beside a beer bottle" style="left:234px;top:329px;width:145px;height:299px;border-radius:24px;background:linear-gradient(180deg,rgba(255,255,255,0) 0%,#f6d79a 18%,#d98a2a 55%,#6b3a12 100%)"></div>
  </section>

  <!-- Panel 3: cover -->
  <section class="panel panel--cover">
    <h1 class="brand-name">Forno Pizza</h1>
    <div class="chef-art" role="img" aria-label="Cartoon chef tossing pizza dough" style="background:radial-gradient(ellipse at 50% 55%,rgba(255,254,252,.85) 0%,rgba(255,254,252,.45) 40%,rgba(236,31,39,0) 70%)"></div>
    <div class="info-band">
      <div class="open-box"><div class="open">OPEN</div>7 DAYS<br>A WEEK</div>
      <div class="hours">
        MONDAY - THURSDAY | 10:30 A.M. - 9:30 P.M.<br>
        FRIDAY &amp; SATURDAY | 10:30 A.M.- 10:00 P.M.<br>
        SUNDAY | 12:00 NOON - 8:00 P.M.<br>
        <span class="accent">Major Credit Cards Accepted</span><br>
        <span class="service">DINE-IN and CARRY OUT</span>
      </div>
      <div class="edge-bar"></div>
    </div>
  </section>

</main>
</body>
</html>
```